Brimvale Crest Homes needs a business card

We need a business card for a new company in Canada, Ontario. Our company is all about luxury contraction homes for our clients. Our product and services are custom projects design. Under the business logo that will be created, we want a slogan that will be a memorable phrase for consumers to remember us to tell their friends and relatives.

Additional infomation
- Teodoro Vanlesky
- President / Ceo
-519.304.7718

Find point what luxury construction products and services can be done

We like to see colors:
- #663300
- and something other colors or color that would attract the client needs and wants

The final design should communicate leads from new or old clients that will grow our empire. Most of all, we try to work among the budget that clients want

NOTE
- we also need an icon for the business (Example: Instagram, Facebook, and Whatsapp icons)
- We want the company name to be remembered easily for clients and our distributors who would get our orders.
- we need an icon on the business cards: Facebook and Instagram.

Thanks,
Brimvale Crest Homes

```html
<!DOCTYPE html>
<html lang="en">
<head>
<meta charset="utf-8">
<title>Brimvale Crest Homes – Business Card</title>
<link rel="stylesheet" href="https://fonts.googleapis.com/css2?family=Open+Sans:wght@400;700&display=swap">
<style>
  :root {
    --backdrop: #262626;
    --card: #0e0e0e;
    --card-edge: #161616;
    --bronze: #663300;
    --bronze-text: #7a3f0c;
    --rule: #4a2a0c;
  }
  * { margin: 0; padding: 0; box-sizing: border-box; }
  html, body {
    width: 1200px;
    height: 900px;
    overflow: hidden;
    background: var(--backdrop);
    font-family: "Open Sans", Arial, sans-serif;
  }
  .canvas {
    position: relative;
    width: 1200px;
    height: 900px;
  }
  .card {
    position: absolute;
    left: 337px;
    width: 526px;
    height: 300px;
    background: linear-gradient(180deg, var(--card-edge), var(--card));
    border-bottom: 9px solid var(--bronze);
    box-shadow: 0 10px 30px rgba(0, 0, 0, 0.45);
    color: var(--bronze-text);
    text-align: center;
  }
  .card--front { top: 110px; }
  .card--back { top: 470px; }

  .brand {
    position: absolute;
    top: 108px;
    left: 0;
    right: 0;
  }
  .brand__name {
    font-weight: 700;
    font-size: 34px;
    letter-spacing: 0.5px;
    line-height: 1;
  }
  .brand__tagline {
    margin-top: 10px;
    font-size: 12.5px;
    letter-spacing: 1.2px;
    text-transform: uppercase;
  }

  .contact {
    position: absolute;
    top: 52px;
    left: 0;
    right: 0;
  }
  .contact__name {
    font-weight: 700;
    font-size: 27px;
    letter-spacing: 1px;
    text-transform: uppercase;
    line-height: 1.1;
  }
  .contact__title {
    font-size: 19px;
    line-height: 1.3;
  }
  .rule {
    height: 1px;
    background: var(--rule);
    margin: 8px auto;
  }
  .rule--wide { width: 260px; }
  .rule--narrow { width: 250px; }
  .contact__phone {
    font-size: 25px;
    letter-spacing: 1px;
    line-height: 1.2;
  }
  .social {
    display: flex;
    justify-content: center;
    gap: 8px;
    margin-top: 4px;
  }
  .social__dot {
    width: 30px;
    height: 30px;
    border-radius: 50%;
    background: var(--bronze-text);
  }
</style>
</head>
<body>
<main class="canvas">
  <section class="card card--front">
    <div class="brand">
      <div class="brand__name">Brimvale Crest Homes</div>
      <div class="brand__tagline">- Home Renovations · Custom Project Design -</div>
    </div>
  </section>

  <section class="card card--back">
    <div class="contact">
      <div class="contact__name">Teodoro Vanlesky</div>
      <div class="contact__title">President / CEO</div>
      <div class="rule rule--wide"></div>
      <div class="contact__phone">519.304.7718</div>
      <div class="rule rule--narrow"></div>
      <div class="social" aria-label="Social media">
        <span class="social__dot"></span>
        <span class="social__dot"></span>
      </div>
      <div class="rule rule--narrow"></div>
    </div>
  </section>
</main>
</body>
</html>
```